Varlo Build for Rent Development Company

We are a new multifamily, build for rent, development company that is looking to build a pitch book outlining our company along with the real estate opportunity. We would want the style to be a modern, clean aesthetic with cool colors

```html
<!DOCTYPE html>
<html lang="en">
<head>
<meta charset="utf-8">
<title>Varlo Pitch Book</title>
<link href="https://fonts.googleapis.com/css2?family=Sora:wght@400;500;600;700&family=Open+Sans:wght@400;600;700&display=swap" rel="stylesheet">
<style>
:root{
  --canvas:#cfdfea;
  --navy:#131b28;
  --blue:#3a6b96;
  --blue-dark:#2f5f8a;
  --sky:#9fbcd2;
  --panel:#e0ebf3;
  --ink:#1a2230;
  --text:#3b4452;
  --white:#ffffff;
  --line:#c9d3dd;
}
*{margin:0;padding:0;box-sizing:border-box}
html,body{width:1013px;height:1200px;overflow:hidden}
body{background:var(--canvas);font-family:"Open Sans",sans-serif;color:var(--ink);position:relative}
.slide{position:absolute;width:715px;height:402px;transform:scale(.5743);transform-origin:0 0;overflow:hidden;background:var(--white);box-shadow:0 8px 18px rgba(20,40,60,.25)}
.slide.dark{background:var(--navy)}
.col-l{left:78px}.col-r{left:525px}
.row-1{top:89px}.row-2{top:352.6px}.row-3{top:616.2px}.row-4{top:879.8px}
.abs{position:absolute}
.brand{position:absolute;right:37px;top:22px;font-family:"Sora",sans-serif;font-weight:700;font-size:13px;color:var(--blue);letter-spacing:.3px}
.title{position:absolute;left:37px;top:18px;font-family:"Sora",sans-serif;font-weight:500;font-size:28px;color:var(--ink)}
.title-rule{position:absolute;left:37px;top:61px;width:22px;height:2px;background:var(--blue)}
.kicker{position:absolute;left:37px;top:78px;font-weight:700;font-size:11.5px;color:var(--blue)}
.lede{position:absolute;left:36px;top:97px;font-size:9.5px;color:var(--text)}
.footer{position:absolute;left:0;right:0;bottom:0;height:20px;background:var(--navy);border-top-left-radius:22px;color:var(--white);font-size:9.5px;display:flex;justify-content:space-between;align-items:center;padding:0 37px 0 37px}
.footer.accent{background:var(--blue)}
.photo{position:absolute}
/* cover */
.cover-brand{position:absolute;left:36px;top:72px;font-family:"Sora",sans-serif;font-weight:700;font-size:27px;color:var(--blue)}
.cover-head{position:absolute;left:37px;font-family:"Sora",sans-serif;font-weight:600;color:var(--white);line-height:1.05}
.cover-sub{position:absolute;left:37px;color:var(--white);font-size:9.5px;line-height:1.55}
.cover-bar{position:absolute;left:0;width:287px;height:30px;background:var(--blue);color:var(--white);font-size:11px;display:flex;align-items:center;gap:8px;padding-left:37px}
/* cards */
.card{position:absolute;top:134px;width:155px;height:232px;background:var(--panel);clip-path:polygon(0 0,86% 0,100% 8%,100% 100%,14% 100%,0 92%)}
.card .icon{position:absolute;left:14px;top:22px}
.card h3{position:absolute;left:14px;top:78px;font-family:"Sora",sans-serif;font-size:11.5px;font-weight:600;line-height:1.15;color:var(--ink)}
.card p{position:absolute;left:14px;top:118px;width:132px;font-size:8.6px;line-height:15.6px;color:var(--text)}
/* agenda */
.agenda-item{position:absolute;left:37px;width:318px;height:36px;background:var(--white);border-radius:3px;box-shadow:0 1px 5px rgba(30,50,70,.18);display:flex;align-items:center;padding-left:20px;font-size:11px;font-weight:600;color:var(--ink)}
.agenda-item span{color:var(--blue);margin-right:6px}
/* table */
.cell{position:absolute;height:28px;border:1px solid var(--line);font-size:8px;display:flex;align-items:center;padding-left:14px;color:var(--ink)}
.cell.head{border:none;color:var(--white);font-weight:700;font-size:8.5px;background:var(--navy)}
.cell.head.metric{background:var(--blue)}
.checklist{position:absolute;left:566px;top:132px;font-size:9.5px;color:var(--text);list-style:none}
.checklist li{height:25px;display:flex;align-items:center;gap:6px}
/* company */
.pillar{position:absolute;top:158px;width:200px}
.pillar .badge{width:56px;height:56px;border-radius:50%;background:var(--white);box-shadow:0 1px 6px rgba(30,50,70,.25);display:flex;align-items:center;justify-content:center}
.pillar h3{margin-top:20px;font-size:11px;font-weight:700;color:var(--ink)}
.pillar p{margin-top:8px;font-size:9px;line-height:18px;color:var(--text)}
/* team */
.member{position:absolute;top:134px;width:155px;height:232px;background:var(--panel);clip-path:polygon(0 0,86% 0,100% 8%,100% 100%,14% 100%,0 92%);text-align:center}
.member .portrait{position:absolute;left:12px;top:13px;width:130px;height:84px;clip-path:polygon(0 0,84% 0,100% 22%,100% 100%,0 100%)}
.member h3{position:absolute;left:0;right:0;top:114px;font-family:"Sora",sans-serif;font-size:11.5px;font-weight:600}
.member .role{position:absolute;left:0;right:0;top:131px;font-size:8.6px;font-weight:700;color:var(--blue)}
.member p{position:absolute;left:8px;right:8px;top:147px;font-size:8.6px;line-height:15.6px;color:var(--text)}
/* section + closing */
.section-title{position:absolute;left:37px;top:140px;font-family:"Sora",sans-serif;font-weight:500;font-size:29px;color:var(--white)}
.section-sub{position:absolute;left:37px;top:196px;font-size:16px;color:var(--white)}
</style>
</head>
<body>

<!-- Cover -->
<section class="slide dark col-l row-1">
  <svg class="abs" style="left:0;top:0" width="715" height="402" viewBox="0 0 715 402">
    <defs>
      <linearGradient id="gBuild1" x1="0" y1="0" x2="0" y2="1">
        <stop offset="0" stop-color="#c9ced6"/><stop offset=".45" stop-color="#b98a5c"/><stop offset=".8" stop-color="#6c6a52"/><stop offset="1" stop-color="#8d7a64"/>
      </linearGradient>
    </defs>
    <ellipse cx="720" cy="215" rx="400" ry="300" fill="var(--blue-dark)"/>
    <ellipse cx="742" cy="215" rx="396" ry="292" fill="var(--navy)"/>
    <ellipse cx="752" cy="228" rx="384" ry="282" fill="var(--sky)"/>
    <ellipse cx="760" cy="215" rx="382" ry="280" fill="url(#gBuild1)" role="img" aria-label="Photo of a modern multifamily apartment building with landscaped walkway"/>
  </svg>
  <div class="cover-brand">VARLO</div>
  <div class="cover-head" style="top:145px;font-size:39px">Multifamily.<br>Built for Rent.</div>
  <div class="cover-sub" style="top:239px">A modern development platform creating high-quality<br>rental communities designed for durable, long-term value.</div>
  <div class="cover-bar" style="top:319px">
    <svg width="11" height="11" viewBox="0 0 12 12" fill="none" stroke="#fff" stroke-width="1.2"><rect x="1" y="2" width="10" height="9" rx="1"/><path d="M1 5h10M4 1v2M8 1v2"/></svg>
    Wednesday, 12 August 2026
  </div>
</section>

<!-- Investment Thesis -->
<section class="slide col-r row-1">
  <div class="title">Investment Thesis</div><div class="title-rule"></div>
  <div class="brand">VARLO</div>
  <div class="kicker">Why Varlo, why now</div>
  <div class="lede">A clear strategy built around durable housing demand and a scalable development model.</div>

  <div class="card" style="left:37px">
    <svg class="icon" width="34" height="36" viewBox="0 0 34 36" fill="var(--blue)"><path d="M14 2h6v10h5l-8 9-8-9h5z"/><path d="M2 24h6l6 3h8a2 2 0 0 1 0 4h-8v1h9l8-5 2 2-9 7H2z"/></svg>
    <h3>Structural<br>demand</h3>
    <p>Renters increasingly value flexibility, privacy, quality and amenity-rich communities without the responsibilities of homeownership.</p>
  </div>
  <div class="card" style="left:198px">
    <svg class="icon" width="40" height="36" viewBox="0 0 40 36" fill="var(--blue)"><path d="M2 14h10l6 8-6 8H2l6-8zM16 14h10l6 8-6 8H16l6-8z"/><path d="M30 14h4l6 8-6 8h-4l6-8z"/><path d="M4 4l3 3 4-5M16 4l3 3 4-5M28 4l3 3 4-5" stroke="var(--blue)" stroke-width="2" fill="none"/></svg>
    <h3>Fragmented<br>supply</h3>
    <p>Much of the rental housing stock is aging or not purpose-designed for the needs of today's renter.</p>
  </div>
  <div class="card" style="left:361px">
    <svg class="icon" width="36" height="36" viewBox="0 0 36 36"><rect x="2" y="20" width="14" height="14" fill="var(--blue)"/><path d="M8 2h26v26H8z" fill="none" stroke="var(--blue)" stroke-width="3"/><path d="M14 22L30 6M21 6h9v9" stroke="var(--blue)" stroke-width="3" fill="none"/></svg>
    <h3>Scalable model</h3>
    <p>Standardized planning &amp; design can reduce complexity, improve execution and create repeatable economics across markets.</p>
  </div>
  <div class="card" style="left:522px">
    <svg class="icon" width="36" height="36" viewBox="0 0 36 36" fill="none" stroke="var(--blue)" stroke-width="2.5"><circle cx="19" cy="19" r="14"/><path d="M19 11v9l6 4"/><path d="M6 8l-2-4M3 12H0" stroke-dasharray="2 2"/></svg>
    <h3>Long-term<br>value</h3>
    <p>Well-located, well-operated communities can support resilient occupancy, strong resident retention and institutional appeal.</p>
  </div>
  <div class="footer"><span>2026 Varlo. All Rights Reserved.</span><span>05</span></div>
</section>

<!-- Agenda -->
<section class="slide col-l row-2">
  <svg class="abs" style="left:0;top:0" width="715" height="402" viewBox="0 0 715 402" role="img" aria-label="Photo of a contemporary two-storey residence at dusk with lit windows">
    <defs>
      <linearGradient id="gSky" x1="0" y1="0" x2="0" y2="1"><stop offset="0" stop-color="#a9bdd0"/><stop offset=".5" stop-color="#d7dde3"/><stop offset=".75" stop-color="#4e4a48"/><stop offset="1" stop-color="#9aa39b"/></linearGradient>
      <linearGradient id="gFade" x1="0" y1="0" x2="1" y2="0"><stop offset=".22" stop-color="#fff"/><stop offset=".55" stop-color="#fff" stop-opacity="0"/></linearGradient>
    </defs>
    <rect x="120" y="0" width="595" height="382" fill="url(#gSky)"/>
    <rect x="0" y="0" width="715" height="382" fill="url(#gFade)"/>
  </svg>
  <div class="title">Agenda</div><div class="title-rule"></div>
  <div class="brand">VARLO</div>
  <div class="agenda-item" style="top:86px"><span>01.</span>Introduction</div>
  <div class="agenda-item" style="top:131px"><span>02.</span>Product</div>
  <div class="agenda-item" style="top:175px"><span>03.</span>Development Strategy</div>
  <div class="agenda-item" style="top:220px"><span>04.</span>Economic Model</div>
  <div class="agenda-item" style="top:264px"><span>05.</span>Pipeline</div>
  <div class="agenda-item" style="top:309px"><span>06.</span>Partnership</div>
  <div class="footer"><span>2026 Varlo. All Rights Reserved.</span><span>02</span></div>
</section>

<!-- Economic Model -->
<section class="slide col-r row-2">
  <div class="title">Economic Model</div><div class="title-rule"></div>
  <div class="brand">VARLO</div>
  <div class="kicker">Designed for disciplined, repeatable returns</div>
  <div class="lede">Illustrative framework — replace placeholders with Varlo's underwriting assumptions.</div>

  <div class="cell head metric" style="left:37px;top:128px;width:175px">Metric</div>
  <div class="cell head" style="left:220px;top:128px;width:101px">Base Case</div>
  <div class="cell head" style="left:327px;top:128px;width:101px">Upside</div>
  <div class="cell head" style="left:435px;top:128px;width:101px">Downside</div>

  <div class="cell" style="left:37px;top:160px;width:175px">Units</div>
  <div class="cell" style="left:220px;top:160px;width:101px">XXX</div>
  <div class="cell" style="left:327px;top:160px;width:101px">XXX</div>
  <div class="cell" style="left:435px;top:160px;width:101px">XXX</div>

  <div class="cell" style="left:37px;top:193px;width:175px">Avg. Rent / Month</div>
  <div class="cell" style="left:220px;top:193px;width:101px">$X,XXX</div>
  <div class="cell" style="left:327px;top:193px;width:101px">$X,XXX</div>
  <div class="cell" style="left:435px;top:193px;width:101px">$X,XXX</div>

  <div class="cell" style="left:37px;top:226px;width:175px">Development Cost / Unit</div>
  <div class="cell" style="left:220px;top:226px;width:101px">$XXX,XXX</div>
  <div class="cell" style="left:327px;top:226px;width:101px">$XXX,XXX</div>
  <div class="cell" style="left:435px;top:226px;width:101px">$XXX,XXX</div>

  <div class="cell" style="left:37px;top:259px;width:175px">Stabilized Occupancy</div>
  <div class="cell" style="left:220px;top:259px;width:101px">XX%</div>
  <div class="cell" style="left:327px;top:259px;width:101px">XX%</div>
  <div class="cell" style="left:435px;top:259px;width:101px">XX%</div>

  <div class="cell" style="left:37px;top:292px;width:175px">Yield on Cost</div>
  <div class="cell" style="left:220px;top:292px;width:101px">X.X%</div>
  <div class="cell" style="left:327px;top:292px;width:101px">X.X%</div>
  <div class="cell" style="left:435px;top:292px;width:101px">X.X%</div>

  <div class="cell" style="left:37px;top:325px;width:175px">Exit Cap Rate</div>
  <div class="cell" style="left:220px;top:325px;width:101px">X.X%</div>
  <div class="cell" style="left:327px;top:325px;width:101px">X.X%</div>
  <div class="cell" style="left:435px;top:325px;width:101px">X.X%</div>

  <ul class="checklist">
    <li>Key diligence:</li>
    <li><svg width="9" height="9" viewBox="0 0 10 10"><path d="M1 5l3 3 5-7" stroke="var(--blue)" stroke-width="1.8" fill="none"/></svg>Land basis</li>
    <li><svg width="9" height="9" viewBox="0 0 10 10"><path d="M1 5l3 3 5-7" stroke="var(--blue)" stroke-width="1.8" fill="none"/></svg>Construction costs</li>
    <li><svg width="9" height="9" viewBox="0 0 10 10"><path d="M1 5l3 3 5-7" stroke="var(--blue)" stroke-width="1.8" fill="none"/></svg>Financing</li>
    <li><svg width="9" height="9" viewBox="0 0 10 10"><path d="M1 5l3 3 5-7" stroke="var(--blue)" stroke-width="1.8" fill="none"/></svg>Rent comps</li>
    <li><svg width="9" height="9" viewBox="0 0 10 10"><path d="M1 5l3 3 5-7" stroke="var(--blue)" stroke-width="1.8" fill="none"/></svg>Absorption</li>
    <li><svg width="9" height="9" viewBox="0 0 10 10"><path d="M1 5l3 3 5-7" stroke="var(--blue)" stroke-width="1.8" fill="none"/></svg>Operating expenses</li>
    <li><svg width="9" height="9" viewBox="0 0 10 10"><path d="M1 5l3 3 5-7" stroke="var(--blue)" stroke-width="1.8" fill="none"/></svg>Exit liquidity</li>
  </ul>
  <div class="footer"><span>2026 Varlo. All Rights Reserved.</span><span>06</span></div>
</section>

<!-- Company -->
<section class="slide col-l row-3">
  <div class="title">Company</div><div class="title-rule"></div>
  <div class="brand">VARLO</div>
  <div class="kicker">A focused platform for the next generation of rental living</div>
  <div class="lede">Varlo combines disciplined development, thoughtful design and institutional-quality execution.</div>

  <div class="pillar" style="left:37px">
    <div class="badge"><svg width="26" height="24" viewBox="0 0 26 24" fill="var(--navy)"><path d="M13 1l12 6-12 6L1 7z"/><path d="M1 12l12 6 12-6-2-1-10 5L3 11z"/><path d="M1 17l12 6 12-6-2-1-10 5L3 16z"/></svg></div>
    <h3>THE PLATFORM</h3>
    <p>Developing purpose-built rental communities with a repeatable approach to site selection, design, construction and operations.</p>
  </div>
  <div class="pillar" style="left:261px">
    <div class="badge"><svg width="22" height="24" viewBox="0 0 22 24"><rect x="1" y="1" width="20" height="22" rx="2" fill="var(--navy)"/><rect x="7" y="1" width="8" height="8" fill="#fff"/><rect x="12" y="17" width="6" height="2" fill="#fff"/></svg></div>
    <h3>THE PRODUCT</h3>
    <p>Modern homes, connected amenities and neighborhood-scale planning designed around how today's renters actually live.</p>
  </div>
  <div class="pillar" style="left:484px">
    <div class="badge"><svg width="28" height="26" viewBox="0 0 28 26" fill="var(--navy)"><circle cx="15" cy="8" r="4.5"/><rect x="13.5" y="12" width="3" height="3"/><path d="M15 0v1.5M8 3l1 1M22 3l-1 1M6 8h1.5M22.5 8H24" stroke="var(--blue)" stroke-width="1.3"/><path d="M1 17h5l5 2h6a1.5 1.5 0 0 1 0 3h-6v1h7l7-4 2 2-8 5H1z"/></svg></div>
    <h3>THE OPPORTUNITY</h3>
    <p>Build-to-rent creates an attractive intersection of housing demand, operational scale and long-duration real estate value.</p>
  </div>
  <div class="footer"><span>2026 Varlo. All Rights Reserved.</span><span>03</span></div>
</section>

<!-- Team -->
<section class="slide col-r row-3">
  <div class="title">Team</div><div class="title-rule"></div>
  <div class="brand">VARLO</div>
  <div class="kicker">Experienced people. Aligned incentives. Focused execution.</div>
  <div class="lede">Introduce the founders and senior team with concise bios emphasizing development, capital, construction and operations expertise</div>

  <div class="member" style="left:37px">
    <div class="portrait" role="img" aria-label="Portrait photo of the founder and CEO" style="background:linear-gradient(135deg,#6d7782,#a48a72 60%,#3d4048)"></div>
    <h3>Owen Hartley</h3><div class="role">Founder / CEO</div>
    <p>Nemo enim ipsam voluptate quia voluptas sit aspernatur aut odit aut fugit, sed quia consequuntur magni dolo.</p>
  </div>
  <div class="member" style="left:198px">
    <div class="portrait" role="img" aria-label="Portrait photo of the head of development" style="background:linear-gradient(135deg,#6b3f2a,#4a3329 60%,#2c2a2c)"></div>
    <h3>Marcus Bennett</h3><div class="role">Development</div>
    <p>Nemo enim ipsam voluptate quia voluptas sit aspernatur aut odit aut fugit, sed quia consequuntur magni dolo.</p>
  </div>
  <div class="member" style="left:361px">
    <div class="portrait" role="img" aria-label="Portrait photo of the capital markets lead" style="background:linear-gradient(135deg,#8c6a4c,#b68d6a 55%,#5a4a3e)"></div>
    <h3>Daniel Reyes</h3><div class="role">Capital Markets</div>
    <p>Nemo enim ipsam voluptate quia voluptas sit aspernatur aut odit aut fugit, sed quia consequuntur magni dolo.</p>
  </div>
  <div class="member" style="left:522px">
    <div class="portrait" role="img" aria-label="Portrait photo of the construction lead" style="background:linear-gradient(135deg,#2e3f57,#4a3a34 55%,#25324a)"></div>
    <h3>Elliot Grant</h3><div class="role">Construction</div>
    <p>Nemo enim ipsam voluptate quia voluptas sit aspernatur aut odit aut fugit, sed quia consequuntur magni dolo.</p>
  </div>
  <div class="footer"><span>2026 Varlo. All Rights Reserved.</span><span>07</span></div>
</section>

<!-- Section divider -->
<section class="slide dark col-l row-4">
  <svg class="abs" style="left:0;top:0" width="715" height="402" viewBox="0 0 715 402">
    <defs>
      <linearGradient id="gCouple" x1="0" y1="0" x2="1" y2="1"><stop offset="0" stop-color="#dfe3e6"/><stop offset=".45" stop-color="#a88a72"/><stop offset="1" stop-color="#59666c"/></linearGradient>
    </defs>
    <ellipse cx="730" cy="290" rx="400" ry="250" fill="var(--blue-dark)"/>
    <ellipse cx="752" cy="292" rx="392" ry="242" fill="var(--navy)"/>
    <ellipse cx="760" cy="300" rx="382" ry="236" fill="var(--sky)"/>
    <ellipse cx="768" cy="292" rx="380" ry="232" fill="url(#gCouple)" role="img" aria-label="Photo of a smiling couple shaking hands with a leasing agent in a new home"/>
  </svg>
  <div class="brand">VARLO</div>
  <div class="section-title">Investment Thesis</div>
  <div class="title-rule" style="top:182px;background:var(--blue)"></div>
  <div class="section-sub">Why Varlo, why now</div>
  <div class="footer accent"><span>2026 Varlo. All Rights Reserved.</span><span>04</span></div>
</section>

<!-- Closing -->
<section class="slide dark col-r row-4">
  <svg class="abs" style="left:0;top:0" width="715" height="402" viewBox="0 0 715 402">
    <defs>
      <linearGradient id="gKeys" x1="0" y1="0" x2="1" y2="1"><stop offset="0" stop-color="#8ea36a"/><stop offset=".45" stop-color="#c9a58a"/><stop offset=".75" stop-color="#3f6d95"/><stop offset="1" stop-color="#9aa3ab"/></linearGradient>
    </defs>
    <ellipse cx="720" cy="215" rx="400" ry="295" fill="var(--blue-dark)"/>
    <ellipse cx="742" cy="215" rx="392" ry="287" fill="var(--navy)"/>
    <ellipse cx="752" cy="228" rx="382" ry="278" fill="var(--sky)"/>
    <ellipse cx="760" cy="215" rx="380" ry="275" fill="url(#gKeys)" role="img" aria-label="Photo of a hand passing house keys to a smiling new resident"/>
  </svg>
  <div class="cover-brand" style="top:56px">VARLO</div>
  <div class="cover-head" style="top:112px;font-size:37px;line-height:1.13">Building the<br>future of<br>rental living.</div>
  <div class="cover-sub" style="top:250px;font-size:8.8px">Modern homes. Strong communities. Disciplined<br>real estate.</div>
  <div class="cover-bar" style="top:318px">
    <svg width="11" height="11" viewBox="0 0 12 12" fill="none" stroke="#fff" stroke-width="1.1"><circle cx="6" cy="6" r="5"/><ellipse cx="6" cy="6" rx="2.2" ry="5"/><path d="M1 6h10"/></svg>
    www.varlo.com
  </div>
</section>

</body>
</html>
```